Trade show banner and popup for Plexa Works

Use the existing logo and graphic elements and text of sales arguments from our web site www.plexaworks-demo.com to create a backdrop banner and popup banner.

Both banners are trim size 181.7 x 76.2 cm. One is vertical, the other is horizontal. The full bleed size is 767 x 1824 mm 2265 x 5385 pixels.

We have a 2m by 2m corner stand on a tradeshow. The banner will be on one wall, the vertical against the other wall by the aisle.

Target Market(s)

This display is for a manufacturing trade show. The typical visitors are middle age engineers.

Industry/Entity Type

Trade

Requirements
Must have
• Our logo.
Nice to have
• One of the main benefits of our system is that it can be created for no charge with an online signup which is available at the show. We want to tempt people off the aisles to do this. So the vertical banner could have the words "Create your own online ERP system here for no charge"
Should not have
• Small text, these banners should attract attention of passers by in a trade show.

```html
<!DOCTYPE html>
<html lang="en">
<head>
<meta charset="utf-8">
<title>Plexa Works – Free Online ERP Banner</title>
<link rel="stylesheet" href="https://fonts.googleapis.com/css2?family=Oswald:wght@500;600;700&display=swap">
<style>
  :root {
    --red: #d4201c;
    --red-deep: #a51410;
    --ink: #1c1c1c;
    --charcoal: #3a3a3a;
    --white: #ffffff;
    --sky: #9fc3de;
    --sea: #7b9fb4;
    --sand: #c9c2ae;
  }
  html, body {
    margin: 0;
    padding: 0;
    width: 1200px;
    height: 2870px;
    overflow: hidden;
    background: var(--white);
  }
  .banner {
    display: block;
    width: 1200px;
    height: 2870px;
  }
  .headline {
    font-family: "Oswald", "Arial Narrow", sans-serif;
    font-weight: 700;
    text-anchor: middle;
  }
  .headline--red { fill: var(--red); }
  .headline--black { fill: var(--ink); }
  .strapline {
    font-family: "Oswald", "Arial Narrow", sans-serif;
    font-weight: 600;
    fill: var(--white);
    text-anchor: middle;
  }
  .brand-name {
    font-family: "Oswald", "Arial Narrow", sans-serif;
    font-weight: 600;
    fill: var(--charcoal);
  }
  .brand-tagline {
    font-family: "Oswald", "Arial Narrow", sans-serif;
    font-weight: 500;
    fill: var(--ink);
    text-anchor: middle;
  }
</style>
</head>
<body>
<svg class="banner" viewBox="0 0 1200 2870" xmlns="http://www.w3.org/2000/svg">
  <defs>
    <linearGradient id="panel-red" x1="0" y1="0" x2="0" y2="1">
      <stop offset="0" stop-color="var(--red)"/>
      <stop offset="0.5" stop-color="#c81b17"/>
      <stop offset="1" stop-color="var(--red-deep)"/>
    </linearGradient>
    <linearGradient id="photo-tones" x1="0" y1="0" x2="0" y2="1">
      <stop offset="0" stop-color="var(--sky)"/>
      <stop offset="0.55" stop-color="var(--sea)"/>
      <stop offset="1" stop-color="var(--sand)"/>
    </linearGradient>
  </defs>

  <!-- red backdrop -->
  <rect class="backdrop" x="0" y="0" width="1200" height="2870" fill="url(#panel-red)"/>

  <!-- hero photo window -->
  <ellipse class="hero-frame" cx="600" cy="-40" rx="640" ry="432" fill="var(--charcoal)"/>
  <ellipse class="hero-photo" cx="600" cy="-40" rx="622" ry="418" fill="url(#photo-tones)"
           role="img" aria-label="Photo of a businessman in a suit with arms raised on a seaside promenade"/>

  <!-- strapline -->
  <text class="strapline" x="600" y="612" font-size="88" textLength="1064" lengthAdjust="spacingAndGlyphs">FREE ONLINE ERP SOLUTION</text>

  <!-- central message disc -->
  <ellipse class="message-rim" cx="600" cy="1545" rx="655" ry="905" fill="var(--ink)"/>
  <ellipse class="message-disc" cx="600" cy="1545" rx="645" ry="858" fill="var(--white)"/>

  <text class="headline headline--red" x="600" y="1051" font-size="205" textLength="600" lengthAdjust="spacingAndGlyphs">SIGN UP</text>
  <text class="headline headline--black" x="600" y="1224" font-size="190" textLength="920" lengthAdjust="spacingAndGlyphs">CREATE YOUR</text>
  <text class="headline headline--red" x="600" y="1413" font-size="215" textLength="920" lengthAdjust="spacingAndGlyphs">OWN ONLINE</text>
  <text class="headline headline--red" x="600" y="1597" font-size="210" textLength="890" lengthAdjust="spacingAndGlyphs">ERP SYSTEM</text>
  <text class="headline headline--black" x="600" y="1766" font-size="195" textLength="560" lengthAdjust="spacingAndGlyphs">HERE FOR</text>
  <text class="headline headline--red" x="600" y="2127" font-size="400" textLength="1070" lengthAdjust="spacingAndGlyphs">NO CHARGE</text>

  <!-- brand footer -->
  <path class="footer-rim" d="M0 2600 Q600 2490 1200 2600 L1200 2870 L0 2870 Z" fill="var(--ink)"/>
  <path class="footer-panel" d="M0 2628 Q600 2520 1200 2628 L1200 2870 L0 2870 Z" fill="var(--white)"/>

  <circle class="brand-mark" cx="205" cy="2735" r="62" fill="var(--charcoal)"/>
  <text class="brand-name" x="290" y="2782" font-size="110">Plexa Works</text>
  <text class="brand-tagline" x="600" y="2850" font-size="44" textLength="944" lengthAdjust="spacing">SIMPLE SMART ANYWHERE</text>
</svg>
</body>
</html>
```